Gold Buyer Business Card

We are looking for a card that catches attention and that someone will remember. It should have a listing of items that we buy as well as a legal disclaimer which will be provided upon request. We have attached our company logo and a photo of a design that I liked for your reference but lets see what the crowd can come up with.
thanks and good luck!!

We Buy Gold & Silver;
Antique Jewelry
Bent/Broken Jewelry
Bracelets
Bullion
Coins
Chains
Dental Gold
Earrings
Rings
Scrap Gold
Silverware/Flatware
Used Jewelry

"Best Price Guaranteed"

Please use graphics of gold jewelry piles. I want some white in order for someone to write on.

Reason: I am looking for more designs with gold jewelry and coins on them. thanks

Industry/Entity Type

Legal

Requirements
Must have
• I would like this to have pictures of gold and silver. Maybe some jewelry in a pile. We are a company that buys scrap gold and jewelry. I would like to see some boldness, this card is a marketing tool and it should leave an impression.
Should not have
• These cards need to promote the company not an individual, no names on the card.

```html
<!DOCTYPE html>
<html lang="en">
<head>
<meta charset="utf-8">
<title>Northgate Metal Traders – Business Card</title>
<link href="https://fonts.googleapis.com/css2?family=Archivo+Black&family=Cinzel:wght@700&family=Open+Sans:wght@400;600&family=Ubuntu:wght@500;700&display=swap" rel="stylesheet">
<style>
  :root {
    --page-bg: #ffffff;
    --card-black: #0b0906;
    --gold: #e2b33c;
    --gold-light: #f7dd7a;
    --gold-deep: #9a6a12;
    --silver-bg: #e4e4e4;
    --silver-light: #f7f7f7;
    --silver-mid: #b9b9b9;
    --ink: #141414;
    --white: #ffffff;
    --badge-red: #c8201a;
  }
  * { box-sizing: border-box; margin: 0; padding: 0; }
  html, body {
    width: 1200px; height: 900px; overflow: hidden;
    background: var(--page-bg);
  }
  .stage {
    position: relative; width: 1200px; height: 900px;
    display: flex; align-items: center; justify-content: center; gap: 40px;
  }
  .card {
    position: relative; width: 540px; height: 340px;
    border-radius: 22px; overflow: hidden;
    box-shadow: 0 10px 28px rgba(0,0,0,0.18);
  }

  /* ---------- Front ---------- */
  .card-front { background: var(--card-black); }
  .coins-photo {
    position: absolute; inset: 0 0 110px 0;
    background:
      radial-gradient(circle at 40% 8%, rgba(255,220,140,0.55), transparent 18%),
      radial-gradient(circle at 58% 4%, rgba(255,220,140,0.45), transparent 14%),
      radial-gradient(ellipse at 50% 85%, rgba(170,120,30,0.55), transparent 60%),
      linear-gradient(180deg, #1a130a 0%, #2b1e0b 100%);
  }
  .coins-strip {
    position: absolute; left: 0; right: 0; bottom: 0; height: 110px;
    background: linear-gradient(180deg, #120d06, #2a1d0a 70%, #5a3f12);
  }
  .brand {
    position: absolute; top: 62px; left: 0; right: 0;
    text-align: center;
    font-family: "Cinzel", serif; font-weight: 700;
    color: var(--gold);
    font-size: 38px; line-height: 1.12; letter-spacing: 1px;
  }
  .gold-rule {
    position: absolute; left: 0; right: 50px; top: 220px; height: 3px;
    background: linear-gradient(90deg, var(--gold-deep), var(--gold-light), var(--gold));
  }
  .gold-rule.lower { top: 322px; right: 0; height: 2px; }
  .contact-list {
    position: absolute; left: 24px; top: 234px;
    list-style: none;
    font-family: "Open Sans", sans-serif; font-size: 15px;
    color: var(--white);
  }
  .contact-list li { display: flex; align-items: center; gap: 10px; height: 20px; }
  .contact-list svg { width: 13px; height: 13px; fill: var(--gold); }
  .bars-photo {
    position: absolute; right: 18px; top: 188px; width: 160px; height: 140px;
    border-radius: 8px;
    background: radial-gradient(ellipse at 55% 55%, var(--gold-light), var(--gold) 45%, var(--gold-deep) 75%, transparent 78%);
  }

  /* ---------- Back ---------- */
  .card-back { background: var(--silver-bg); }
  .silver-photo {
    position: absolute; inset: 0;
    background:
      radial-gradient(ellipse at 60% 40%, rgba(255,255,255,0.7), transparent 55%),
      linear-gradient(180deg, var(--silver-light), var(--silver-bg) 50%, #cfcfcf);
  }
  .title-bar {
    position: absolute; top: 30px; left: 86px; right: 86px; height: 44px;
    background: linear-gradient(180deg, var(--white) 60%, #dcdcdc);
    border-bottom: 3px solid var(--silver-mid);
    display: flex; align-items: center; justify-content: center;
    font-family: "Archivo Black", sans-serif; font-size: 27px; color: var(--ink);
    white-space: nowrap;
  }
  .title-bar .word-gold { color: var(--gold-deep); margin: 0 8px; }
  .title-bar .word-silver { color: #8e8e8e; margin-left: 8px; }
  .bangle-photo {
    position: absolute; top: 18px; width: 64px; height: 82px; border-radius: 50%;
    background: radial-gradient(ellipse, transparent 42%, var(--gold) 46%, var(--gold-deep) 62%, transparent 66%);
  }
  .bangle-photo.left { left: 18px; }
  .bangle-photo.right { right: 18px; }
  .buy-list {
    position: absolute; left: 26px; top: 96px;
    list-style: none;
    font-family: "Ubuntu", sans-serif; font-weight: 700; font-size: 14.5px;
    color: var(--ink); line-height: 19px;
  }
  .buy-list li::before {
    content: ""; display: inline-block; width: 4px; height: 4px;
    background: var(--gold-deep); border-radius: 50%;
    margin-right: 6px; vertical-align: middle;
  }
  .jewelry-photo {
    position: absolute; left: 300px; top: 178px; width: 180px; height: 130px;
    border-radius: 50%;
    background: radial-gradient(ellipse, var(--gold-light), var(--gold) 40%, var(--gold-deep) 68%, transparent 72%);
  }
  .price-badge {
    position: absolute; right: 14px; top: 205px; width: 88px; height: 88px;
    transform: rotate(-35deg);
  }
  .price-badge .ray {
    position: absolute; inset: 12px;
    background: linear-gradient(135deg, var(--gold-light), var(--gold));
  }
  .price-badge .ray:nth-child(2) { transform: rotate(30deg); }
  .price-badge .ray:nth-child(3) { transform: rotate(60deg); }
  .price-badge .badge-text {
    position: absolute; inset: 0;
    display: flex; align-items: center; justify-content: center; text-align: center;
    font-family: "Archivo Black", sans-serif; font-size: 11px; line-height: 1.15;
    color: var(--badge-red);
  }
</style>
</head>
<body>
<main class="stage">

  <section class="card card-front" aria-label="Business card front">
    <div class="coins-photo" role="img" aria-label="Pile of gold coins lit from above"></div>
    <div class="coins-strip" role="img" aria-label="Gold coins background"></div>
    <h1 class="brand">Northgate<br>Metal Traders</h1>
    <div class="gold-rule"></div>
    <ul class="contact-list">
      <li><svg viewBox="0 0 24 24"><path d="M6.6 10.8a15 15 0 0 0 6.6 6.6l2.2-2.2c.3-.3.7-.4 1-.2 1.1.4 2.3.6 3.6.6.6 0 1 .4 1 1V20c0 .6-.4 1-1 1A17 17 0 0 1 3 4c0-.6.4-1 1-1h3.5c.6 0 1 .4 1 1 0 1.3.2 2.5.6 3.6.1.3 0 .7-.2 1z"/></svg>+64 21 555 0142</li>
      <li><svg viewBox="0 0 24 24"><path d="M7 1h10a2 2 0 0 1 2 2v18a2 2 0 0 1-2 2H7a2 2 0 0 1-2-2V3a2 2 0 0 1 2-2zm0 4v13h10V5z"/></svg>+64 9 555 0187</li>
      <li><svg viewBox="0 0 24 24"><path d="M2 5h20v14H2zm2 2v.5l8 5 8-5V7z"/></svg>sales@northgatemetal.co.nz</li>
      <li><svg viewBox="0 0 24 24"><path d="M12 2a10 10 0 1 0 0 20 10 10 0 0 0 0-20zm-1 2.1V8H7.3A8 8 0 0 1 11 4.1zm2 0A8 8 0 0 1 16.7 8H13zM4.3 10h6.7v4H4.3a8 8 0 0 1 0-4zm8.7 0h6.7a8 8 0 0 1 0 4H13zm-5.7 6H11v3.9A8 8 0 0 1 7.3 16zm5.7 0h3.7a8 8 0 0 1-3.7 3.9z"/></svg>www.northgatemetal.co.nz</li>
    </ul>
    <div class="bars-photo" role="img" aria-label="Stack of gold bars with gold rings"></div>
    <div class="gold-rule lower"></div>
  </section>

  <section class="card card-back" aria-label="Business card back">
    <div class="silver-photo" role="img" aria-label="Silver bullion bars and coins in soft focus"></div>
    <div class="bangle-photo left" role="img" aria-label="Gold bangle"></div>
    <div class="bangle-photo right" role="img" aria-label="Gold bangle"></div>
    <h2 class="title-bar">We Buy<span class="word-gold">Gold</span>&amp;<span class="word-silver">Silver</span></h2>
    <ul class="buy-list">
      <li>Antique Jewelry</li>
      <li>Bent/Broken Jewelry</li>
      <li>Bracelets</li>
      <li>Bullion</li>
      <li>Coins</li>
      <li>Chains</li>
      <li>Dental Gold</li>
      <li>Earrings</li>
      <li>Rings</li>
      <li>Scrap Gold</li>
      <li>Silverware/Flatware</li>
      <li>Used Jewelry</li>
    </ul>
    <div class="jewelry-photo" role="img" aria-label="Pile of gold jewelry, rings and chains"></div>
    <div class="price-badge">
      <span class="ray"></span><span class="ray"></span><span class="ray"></span>
      <span class="badge-text">BEST PRICE<br>GUARANTEED</span>
    </div>
  </section>

</main>
</body>
</html>
```